Business card design needed

We are a start up Mobile Vet Clinic.
We will be servicing an are that cover the Gladstone Region Shire.
Bookings will be made via the number listed or email address.
Travel will be charged

Target Market(s)

Pet Owners

Industry/Entity Type

Business

Contact Information for Business Card

BRAMLEY MOBILE VET
Tavestock Pty Ltd
Nora Batterby BVSc
27 Harwick St
Wrenmoor QLD 4695

PH: 0738214069 Fax: 0738214552 email: bmvet@tallowmail.com

Logo styles of interest
Pictorial/Combination Logo

```html
<!DOCTYPE html>
<html lang="en">
<head>
<meta charset="utf-8">
<title>Bramley Mobile Vet – Business Card Options</title>
<link rel="stylesheet" href="https://fonts.googleapis.com/css2?family=Aleo:wght@300;400&family=Open+Sans:wght@300&display=swap">
<style>
  :root {
    --page-bg: #ffffff;
    --option-label: #9cbfc8;
    --card-bg-soft: #f3f3f1;
    --card-bg-white: #ffffff;
    --band: #72a3b0;
    --brand: #1d8199;
    --value: #2a8ea3;
    --muted: #7ea3ad;
    --prefix: #8fb2bb;
    --on-band: #ffffff;
  }
  * { margin: 0; padding: 0; box-sizing: border-box; }
  html, body { width: 1200px; height: 1000px; overflow: hidden; background: var(--page-bg); }
  .board { position: relative; width: 1200px; height: 1000px; font-family: "Aleo", Georgia, serif; }

  .option-label {
    position: absolute; left: 0; width: 1196px; text-align: center;
    font-family: "Open Sans", Arial, sans-serif; font-weight: 300;
    font-size: 20px; line-height: 1; color: var(--option-label);
  }
  .option-label--single { top: 89px; }
  .option-label--double { top: 557px; }

  .card {
    position: absolute; width: 499px; height: 287px; overflow: hidden;
    box-shadow: 0 1px 5px rgba(0,0,0,0.18);
  }
  .card--single { left: 339px; top: 157px; background: var(--card-bg-soft); }
  .card--front  { left: 84px;  top: 616px; }
  .card--back   { left: 619px; top: 616px; background: var(--card-bg-white); }

  .card__line { position: absolute; left: 33px; line-height: 1; white-space: nowrap; }
  .card__name { top: 33px; font-size: 15px; font-weight: 300; color: var(--muted); }
  .contact { font-size: 24px; font-weight: 300; color: var(--value); }
  .contact__prefix { display: inline-block; width: 29px; color: var(--prefix); font-size: 22px; }
  .contact--phone { top: 64px; }
  .contact--fax   { top: 95px; }
  .contact--email { top: 126px; }
  .card__company { top: 168px; font-size: 15px; font-weight: 300; color: var(--muted); }
  .card__address { top: 187px; font-size: 15px; font-weight: 300; color: var(--muted); }

  .card__band {
    position: absolute; left: 0; right: 0; top: 219px; height: 68px;
    background: var(--band); color: var(--on-band);
    font-size: 19px; font-weight: 300; line-height: 66px; padding-left: 33px;
  }

  .wordmark {
    position: absolute; right: 28px; top: 24px; text-align: right;
    font-family: "Aleo", Georgia, serif; font-weight: 400; color: var(--brand); line-height: 1;
  }
  .wordmark__name { display: block; font-size: 38px; }
  .wordmark__tag  { display: block; font-size: 19px; font-weight: 300; margin-top: 2px; padding-right: 10px; }

  .photo-slot--single {
    position: absolute; left: 285px; top: 84px; width: 190px; height: 135px;
    background: radial-gradient(closest-side at 50% 70%, #d9cdb8 0%, #e4dacb 45%, rgba(243,243,241,0) 100%);
  }

  .photo-slot--front {
    position: absolute; inset: 0;
    background: linear-gradient(120deg, #9fb3b8 0%, #c9c4b6 35%, #e4d8c4 55%, #b9c3c3 100%);
  }
  .front__curve { position: absolute; inset: 0; }
  .wordmark--front { color: var(--on-band); right: 36px; top: 44px; }
  .wordmark--front .wordmark__name { font-size: 46px; }
  .wordmark--front .wordmark__tag { font-size: 25px; padding-right: 14px; margin-top: 4px; }
</style>
</head>
<body>
<main class="board">

  <p class="option-label option-label--single">1 sided option</p>

  <section class="card card--single">
    <div class="photo-slot--single" role="img" aria-label="Photo of a woman hugging a yellow labrador puppy"></div>
    <p class="card__line card__name">Nora Batterby BVSc</p>
    <p class="card__line contact contact--phone"><span class="contact__prefix">t</span>0738214069</p>
    <p class="card__line contact contact--fax"><span class="contact__prefix">f</span>0738214552</p>
    <p class="card__line contact contact--email"><span class="contact__prefix">e</span>bmvet@tallowmail.com</p>
    <p class="card__line card__company">Tavestock Pty Ltd</p>
    <p class="card__line card__address">27 Harwick St Wrenmoor QLD 4695</p>
    <div class="wordmark"><span class="wordmark__name">bramley</span><span class="wordmark__tag">mobile vet</span></div>
    <p class="card__band">To book our mobile vet clinic, please get in touch</p>
  </section>

  <p class="option-label option-label--double">2 sided option</p>

  <section class="card card--front">
    <div class="photo-slot--front" role="img" aria-label="Photo of a woman hugging a yellow labrador puppy by the water"></div>
    <svg class="front__curve" width="499" height="287" viewBox="0 0 499 287" aria-hidden="true">
      <path d="M276 0 C300 45 330 72 395 92 C455 110 488 130 499 142 L499 0 Z" fill="var(--band)"/>
    </svg>
    <div class="wordmark wordmark--front"><span class="wordmark__name">bramley</span><span class="wordmark__tag">mobile vet</span></div>
  </section>

  <section class="card card--back">
    <p class="card__line card__name">Nora Batterby BVSc</p>
    <p class="card__line contact contact--phone"><span class="contact__prefix">t</span>0738214069</p>
    <p class="card__line contact contact--fax"><span class="contact__prefix">f</span>0738214552</p>
    <p class="card__line contact contact--email"><span class="contact__prefix">e</span>bmvet@tallowmail.com</p>
    <p class="card__line card__company">Tavestock Pty Ltd</p>
    <p class="card__line card__address">27 Harwick St Wrenmoor QLD 4695</p>
    <div class="wordmark"><span class="wordmark__name">bramley</span><span class="wordmark__tag">mobile vet</span></div>
    <p class="card__band">To book our mobile vet clinic, please get in touch</p>
  </section>

</main>
</body>
</html>
```